Workplace Safety Consultancy Business needs business card design

We need a business card for a new business providing workplace health and safety consulting called 'Worksure Path'. We will be providing small to medium sized businesses assistance with OH&S and HR matters to ensure that their employees and the public are safe in the workplace and that they are meeting their legislative requirements. Would like to see the words 'practical workplace safety solutions' on the card. Personal details on the back. It needs to be clean, smart and professional (no fluff). Would like to see a simple logo if possible as well. Have been looking at orange and black, but open to other ideas.
Updates
Thank you to those to have created designs for us so far! We are really impressed with the impact of the black and orange having now seen it. Would be great if any further designs used those colours. Cheers.

Thank you to everyone that submitted a design. Your work is of the highest quality and we had a hard decision deciding. Sorry if we didn't choose your design, but it just came down to the one that stood out to us personally. Cheers.

Target Market(s)
Small-Medium business owners in Queensland, Australia. Age 25-60 male and female. Initially targeting those in the trade type industries
Industry/Entity Type
Health
Look and feel
Each slider illustrates characteristics of the customer's brand and the style your logo design should communicate.

```html
<!DOCTYPE html>
<html lang="en">
<head>
<meta charset="utf-8">
<title>Worksure Path — Business Card</title>
<link rel="stylesheet" href="https://fonts.googleapis.com/css2?family=Bebas+Neue&family=Open+Sans:wght@400&display=swap">
<style>
  :root {
    --backdrop: #2a2530;
    --card-black: #0d0d0e;
    --card-glow: #2a2a2c;
    --accent-orange: #f7941d;
    --text-white: #f2f2f2;
    --seam-light: rgba(255,255,255,0.14);
    --seam-dark: rgba(0,0,0,0.8);
  }
  * { margin: 0; padding: 0; box-sizing: border-box; }
  html, body {
    width: 1200px; height: 800px; overflow: hidden;
    background: var(--backdrop);
  }
  .canvas {
    width: 1200px; height: 800px;
    display: flex; align-items: center; justify-content: center; gap: 50px;
  }
  .card {
    position: relative;
    width: 525px; height: 300px;
    background: radial-gradient(ellipse at 50% 40%, var(--card-glow) 0%, var(--card-black) 70%);
    box-shadow: 0 12px 30px rgba(0,0,0,0.5);
    overflow: hidden;
  }
  .card__seam {
    position: absolute; top: 0; bottom: 0; width: 2px;
    background: linear-gradient(to right, var(--seam-dark) 0 1px, var(--seam-light) 1px 2px);
  }
  .card__seam::before {
    content: ""; position: absolute; top: 0; bottom: 0; left: -40px; width: 40px;
    background: linear-gradient(to right, transparent, rgba(0,0,0,0.35));
  }

  /* Front */
  .card--front .card__seam { left: 318px; }
  .brand {
    position: absolute; left: 40px; top: 100px;
    text-align: right; width: 262px;
  }
  .brand__name {
    font-family: "Bebas Neue", sans-serif;
    font-size: 54px; line-height: 0.9;
    color: var(--accent-orange); letter-spacing: 0.5px;
    white-space: nowrap;
  }
  .brand__tagline {
    font-family: "Bebas Neue", sans-serif;
    font-size: 15.5px; letter-spacing: 0.3px;
    color: var(--accent-orange); margin-top: 4px;
    white-space: nowrap;
  }
  .brand__mark {
    position: absolute; left: 372px; top: 118px;
    width: 56px; height: 56px;
    background: var(--accent-orange);
  }

  /* Back */
  .card--back .card__seam { left: 278px; }
  .contact {
    position: absolute; right: 262px; top: 108px;
    list-style: none; text-align: right;
    font-family: "Open Sans", sans-serif; font-size: 14.5px;
    line-height: 26px; color: var(--text-white);
    white-space: nowrap;
  }
  .contact-icons {
    position: absolute; left: 292px; top: 112px;
    display: flex; flex-direction: column; gap: 8px;
  }
  .contact-icons svg { width: 17px; height: 17px; fill: var(--accent-orange); display: block; }
  .person-name {
    position: absolute; left: 320px; top: 124px;
    max-width: 185px;
    font-family: "Bebas Neue", sans-serif;
    font-size: 29px; line-height: 1;
    color: var(--accent-orange); white-space: nowrap;
  }
</style>
</head>
<body>
<main class="canvas">

  <section class="card card--front" aria-label="Card front">
    <div class="brand">
      <div class="brand__name">WorksurePath</div>
      <div class="brand__tagline">Practical workplace safety solutions</div>
    </div>
    <div class="card__seam"></div>
    <div class="brand__mark" aria-hidden="true"></div>
  </section>

  <section class="card card--back" aria-label="Card back">
    <ul class="contact">
      <li>0400 555 018</li>
      <li>worksurepath.net.au</li>
      <li>daniel@worksurepath.net.au</li>
    </ul>
    <div class="card__seam"></div>
    <div class="contact-icons" aria-hidden="true">
      <svg viewBox="0 0 20 20"><path d="M3 7c0-2 2-4 7-4s7 2 7 4v2h-4V7H7v2H3z"/><rect x="4" y="10" width="12" height="7" rx="1"/></svg>
      <svg viewBox="0 0 20 20"><rect x="2" y="4" width="16" height="12" rx="1"/><path d="M2 5l8 6 8-6" stroke="#0d0d0e" stroke-width="1.5" fill="none"/></svg>
      <svg viewBox="0 0 20 20"><circle cx="10" cy="10" r="8"/><g stroke="#0d0d0e" stroke-width="1.2" fill="none"><ellipse cx="10" cy="10" rx="3.5" ry="8"/><path d="M2 10h16M3.5 6h13M3.5 14h13"/></g></svg>
    </div>
    <div class="person-name">Daniel Corrigan</div>
  </section>

</main>
</body>
</html>
```